Business Card and Word .doc header and footer required

I need a business card designed for my cybersecurity consulting company. Also required, is a header and footer to be ued for my word documents.
Attached is the Logo design, font and rgb used.

Industry/Entity Type

Cyber Security Consulting

Contact Information for Business Card

Name, Phone, email, website

Colors
0054AA
0677BA
7BADD7
CADEEF
E8F1F8

Requirements
Must have
• Sleek, modern

```html
<!DOCTYPE html>
<html lang="en">
<head>
<meta charset="utf-8">
<title>Halvern Ridge Consulting – Stationery</title>
<link rel="stylesheet" href="https://fonts.googleapis.com/css2?family=Montserrat:wght@500;600;700&display=swap">
<style>
  :root{
    --stage:#bdbec1;
    --navy:#0b1220;
    --blue:#0677ba;
    --blue-deep:#0054aa;
    --blue-light:#7badd7;
    --paper:#ffffff;
    --ghost:#efefef;
    --ink:#4a4d55;
    --white:#f2f4f7;
  }
  *{box-sizing:border-box;margin:0;padding:0}
  html,body{width:1200px;height:1200px;overflow:hidden}
  body{background:var(--stage);font-family:"Montserrat",sans-serif;position:relative}

  .letterhead{position:absolute;left:359px;top:88px;width:791px;height:1024px;background:var(--paper);box-shadow:0 4px 18px rgba(0,0,0,.25);overflow:hidden}
  .letterhead-wave{position:absolute;left:0;top:0;width:260px;height:240px}
  .letterhead-watermark{position:absolute;left:88px;top:176px;width:670px;height:670px}

  .brand{position:absolute;display:flex;flex-direction:column;align-items:center;color:var(--white);font-weight:600;text-align:center;white-space:nowrap;transform:translateX(-50%)}
  .brand-mark{width:52px;height:52px;border:5px solid var(--blue);border-radius:50%;margin-bottom:12px}
  .brand-name{font-size:16px;letter-spacing:.3px;line-height:1}
  .brand-sub{font-size:7px;letter-spacing:3px;margin-top:5px;line-height:1}

  .letterhead .brand{left:96px;top:28px}

  .contact{list-style:none;font-size:10px;line-height:14.5px;color:var(--white);font-weight:500;border-left:1px solid #5a6070;padding-left:9px;white-space:nowrap}
  .contact li{display:flex;align-items:center;gap:4px}
  .contact svg{width:7px;height:7px;fill:var(--blue);flex:none}

  .letterhead-footer{position:absolute;left:560px;top:944px;font-size:13px;line-height:19px;color:var(--ink);border-left-color:#555;padding-left:10px}
  .letterhead-footer svg{width:10px;height:10px}

  .card{position:absolute;width:374px;height:213px;background:var(--navy);border-radius:24px;box-shadow:0 4px 16px rgba(0,0,0,.3);overflow:hidden}
  .card-front{left:66px;top:418px}
  .card-back{left:112px;top:781px}
  .card-front .brand{left:84px;top:16px}
  .card-watermark{position:absolute;left:248px;top:2px;width:136px;height:136px;border:9px solid #23283a;border-radius:50%}
  .card-person{position:absolute;right:186px;top:157px;text-align:right;white-space:nowrap}
  .person-name{font-size:13.5px;font-weight:700;color:var(--blue-light);letter-spacing:.2px;line-height:1}
  .person-role{font-size:11px;font-weight:500;color:var(--white);margin-top:4px}
  .card-front .contact{position:absolute;left:196px;top:155px}
  .card-back .brand{left:50%;top:55px}
  .card-back .brand-mark{width:58px;height:58px}
  .card-back .brand-name{font-size:19px}
</style>
</head>
<body>

<section class="letterhead">
  <svg class="letterhead-wave" viewBox="0 0 260 240" aria-hidden="true">
    <path d="M0,0 H250 C262,80 210,130 140,162 C80,190 30,208 0,235 Z" fill="#0b1220"/>
    <path d="M250,0 C262,80 210,130 140,162 C80,190 30,208 0,235" fill="none" stroke="#0677ba" stroke-width="3"/>
  </svg>
  <div class="brand">
    <span class="brand-mark"></span>
    <span class="brand-name">HALVERN RIDGE</span>
    <span class="brand-sub">CONSULTING</span>
  </div>
  <svg class="letterhead-watermark" viewBox="0 0 670 670" aria-hidden="true">
    <circle cx="335" cy="335" r="312" fill="none" stroke="#efefef" stroke-width="44"/>
  </svg>
  <ul class="contact letterhead-footer">
    <li><svg viewBox="0 0 10 10"><path d="M2 0h2l1 3-1.5 1a6 6 0 0 0 2.5 2.5L7 5l3 1v2c0 1-1 2-2 2A8 8 0 0 1 0 2c0-1 1-2 2-2z"/></svg>555-014-2270</li>
    <li><svg viewBox="0 0 10 10"><path d="M0 2h10v7H0zM0 2l5 4 5-4"/></svg>daniel@halvernridge.com</li>
    <li><svg viewBox="0 0 10 10"><circle cx="5" cy="5" r="5"/></svg>www.halvernridge.com</li>
  </ul>
</section>

<section class="card card-front">
  <span class="card-watermark"></span>
  <div class="brand">
    <span class="brand-mark"></span>
    <span class="brand-name">HALVERN RIDGE</span>
    <span class="brand-sub">CONSULTING</span>
  </div>
  <div class="card-person">
    <p class="person-name">DANIEL REYES</p>
    <p class="person-role">Director</p>
  </div>
  <ul class="contact">
    <li><svg viewBox="0 0 10 10"><path d="M2 0h2l1 3-1.5 1a6 6 0 0 0 2.5 2.5L7 5l3 1v2c0 1-1 2-2 2A8 8 0 0 1 0 2c0-1 1-2 2-2z"/></svg>555-014-2270</li>
    <li><svg viewBox="0 0 10 10"><path d="M0 2h10v7H0z"/></svg>daniel@halvernridge.com</li>
    <li><svg viewBox="0 0 10 10"><circle cx="5" cy="5" r="5"/></svg>www.halvernridge.com</li>
  </ul>
</section>

<section class="card card-back">
  <div class="brand">
    <span class="brand-mark"></span>
    <span class="brand-name">HALVERN RIDGE</span>
    <span class="brand-sub">CONSULTING</span>
  </div>
</section>

</body>
</html>
```